Professional Lighting Providers - Web Design

We need a web design to showcase our ability to provide lighting design and equipment to those who are in need of lighting equipment.

Our 4 markets are:
Broadcasting - Public and Commercial
Education - ISD wide, and private schools
Government - National News, Chamber videos, Press Releases
Religious - Sermon Recording, etc.

We provide lighting products, design consultations(how lights are setup and such), and custom light work.

We want the home page to be setup in a way that someone in one of the 4 markets can drill down into the site. Meaning they are greeted on the home page with 4 large icons or pictures for each market and then they can go farther into the site. We also want a top navigation to be preset so people who are just looking for lighting can also browse our products.

Logo colors are not as they appear on our current website.
#383388 is our current logo color, please also see attachment of logo. In addition, we are just "Clear Beam - Lighting Systems". We dropped the RZ7 out of our name so please don't use it in the concept.

Our Current Site is http://rz7-example.com/index.asp.
We don't have set colors but we know we do not want reds or yellows.

The design should be simple, not cluttered, and not artsy, not fun, but very serious.

Requirements
Must have
• Image banner/slider at the top that slides our 4 products.
Also need to have a form on the home page that will convert visitors to subscribers for a newsletter. Also on every page we want a form were people can send an email off to us asking questions.

```html
<!DOCTYPE html>
<html lang="en">
<head>
<meta charset="utf-8">
<title>Clear Beam Lighting Systems</title>
<link rel="stylesheet" href="https://fonts.googleapis.com/css2?family=Source+Sans+3:wght@300;400;600&family=Pacifico&display=swap">
<style>
:root{
  --brand:#383388;
  --navy:#0f2b55;
  --ink:#1e1e1e;
  --muted:#555;
  --page:#ececea;
  --panel:#f4f4f2;
  --line:#cfcfcf;
  --accent:#1f5fb5;
  --gold:#f2b705;
  --footer:#3a3a3a;
}
*{box-sizing:border-box;margin:0;padding:0}
html,body{width:1108px;height:1200px;overflow:hidden}
body{position:relative;background:var(--page);font-family:"Source Sans 3",Arial,sans-serif;color:var(--ink)}
.abs{position:absolute}
.topbar{left:0;top:0;width:1108px;height:6px;background:var(--navy)}
.header{left:0;top:6px;width:1108px;height:98px;background:linear-gradient(#fafafa,#e6e6e6);border-bottom:1px solid #c8c8c8}
.hero-band{left:0;top:104px;width:1108px;height:404px;background:#f3f3f3}
.logo-box{left:102px;top:6px;width:240px;height:111px;background:#fff;border:1px solid #c9c9c9;border-top:none;border-radius:0 0 10px 10px;box-shadow:0 6px 8px rgba(0,0,0,.08);display:flex;align-items:center;justify-content:center;gap:9px}
.logo-mark{width:18px;height:18px;background:var(--brand);border-radius:50%}
.logo-name{font-size:21px;font-weight:600;color:var(--brand);line-height:1.05}
.nav{left:417px;top:36px;width:527px;height:42px;background:linear-gradient(#fff,#ececec);border:1px solid #bdbdbd;border-radius:6px;display:flex;align-items:center;overflow:hidden}
.nav a{font-size:15px;color:#222;text-decoration:none;padding:0 16px;height:100%;display:flex;align-items:center;border-right:1px solid #cfcfcf}
.nav a:last-child{border-right:none}
.nav a.active{background:linear-gradient(#5a5a5a,#2f2f2f);color:#fff;padding:0 26px}
.slider{left:104px;top:132px;width:901px;height:362px;background:#fff;box-shadow:0 2px 6px rgba(0,0,0,.25)}
.slide-photo{left:8px;top:6px;width:887px;height:349px;background:linear-gradient(90deg,#1c1c24 0%,#243e8a 20%,#3a3a44 45%,#7a6a55 70%,#1e2b5e 90%,#1a1a1a 100%)}
.caption{left:7px;top:295px;width:443px;height:60px;background:rgba(20,20,20,.85);color:#fff;font-size:29px;font-weight:400;display:flex;align-items:center;padding-left:13px}
.dots{left:744px;top:320px;width:151px;height:35px;background:#fff;display:flex;align-items:center;justify-content:center;gap:5px}
.dot{width:19px;height:19px;border-radius:50%;background:radial-gradient(#3a3a3a,#111);border:2px solid #888}
.dot.on{background:radial-gradient(#6cc0ff,#1466c4)}
.arrow{top:275px;width:34px;height:67px}
.cards{left:0;top:508px;width:1108px;height:632px;background:var(--page)}
.card{top:0}
.card-title{font-size:18px;font-weight:400;color:#1e1e1e;position:absolute;top:31px}
.card-frame{position:absolute;top:52px;width:178px;height:78px;background:#f7f7f7;border:1px solid #d6d6d6}
.card-photo{position:absolute;left:4px;top:4px;width:170px;height:62px}
.card-body{position:absolute;top:129px;left:7px;width:164px;height:121px;background:#e4e3e4;border:1px solid #d0d0d0;padding:18px 12px 0;font-size:9px;font-weight:300;line-height:12px;color:#333}
.pin{position:absolute;top:122px;width:16px;height:12px;border-radius:0 0 8px 8px;background:#fff;border:2px solid #2b3a55;border-top:none}
.more{position:absolute;top:244px;width:52px;height:19px;background:linear-gradient(#fff,#e2e2e2);border:1px solid #bbb;font-size:11px;color:#333;display:flex;align-items:center;justify-content:center;box-shadow:0 1px 2px rgba(0,0,0,.2)}
.divider{left:118px;top:828px;width:868px;height:1px;background:var(--line)}
.news-title{left:148px;top:848px;font-size:25px;color:#1e1e1e}
.product-frame{left:148px;top:894px;width:171px;height:197px;background:#f6f6f6;border:1px solid #d8d8d8;padding:6px}
.product-photo{width:100%;height:100%;background:linear-gradient(#e6e6e6,#cfcfcf)}
.posted{left:154px;top:1093px;font-size:11.5px;line-height:16px;color:#222}
.product-name{left:334px;top:888px;font-size:15px;font-weight:600;color:#222}
.features{left:334px;top:917px;list-style:none;font-size:11.5px;line-height:19.4px;color:#222}
.features li::before{content:"";display:inline-block;width:4px;height:4px;border-radius:50%;background:#222;margin:0 9px 2px 1px}
.newsletter{left:605px;top:875px;width:386px;height:238px;background:#fff;border:1px solid #cfcfcf;border-radius:8px}
.nl-head{position:absolute;left:19px;top:4px;font-family:"Pacifico",cursive;font-size:25px;color:var(--accent)}
.nl-sub{position:absolute;left:26px;top:45px;font-family:Arial,sans-serif;font-size:11.5px;color:#666}
.field-label{position:absolute;left:26px;font-family:Arial,sans-serif;font-size:11.5px;color:#555}
.field{position:absolute;left:70px;width:277px;height:37px;border:1px solid #bdbdbd;border-radius:5px;background:linear-gradient(#f2f2f2,#fff)}
.subscribe{position:absolute;left:70px;top:191px;width:114px;height:36px;border:none;border-radius:4px;background:linear-gradient(#ffd43a,#f0a800);font-family:Arial,sans-serif;font-size:13.5px;color:#222;box-shadow:0 2px 0 #c98a00}
.footer{left:0;top:1140px;width:1108px;height:60px;background:linear-gradient(#555,#2b2b2b);border-top:2px solid #7a7a7a;color:#fff;text-align:center}
.footer nav{margin-top:8px;font-size:11.5px}
.footer nav a{color:#fff;text-decoration:none;margin:0 15px}
.footer p{font-size:10.5px;margin-top:3px;color:#eee}
</style>
</head>
<body>
<div class="abs topbar"></div>
<div class="abs header"></div>
<div class="abs hero-band"></div>

<div class="abs logo-box">
  <span class="logo-mark"></span>
  <span class="logo-name">Clear Beam<br>Lighting Systems</span>
</div>

<nav class="abs nav">
  <a class="active" href="#">HOME</a>
  <a href="#">ABOUT US</a>
  <a href="#">PRODUCTS</a>
  <a href="#">LATEST NEWS</a>
  <a href="#">CONTACT US</a>
</nav>

<svg class="abs arrow" style="left:72px" viewBox="0 0 34 67"><path d="M34 0A34 34 0 0 0 34 67Z" fill="#14395f"/><path d="M22 24 13 33.5 22 43" stroke="#fff" stroke-width="5" fill="none"/></svg>
<svg class="abs arrow" style="left:1006px" viewBox="0 0 34 67"><path d="M0 0A34 34 0 0 1 0 67Z" fill="#14395f"/><path d="M11 24 20 33.5 11 43" stroke="#fff" stroke-width="5" fill="none"/></svg>

<section class="abs slider">
  <div class="abs slide-photo" role="img" aria-label="Broadcast studio with news desk, cameras and blue and amber lighting">
    <div class="abs caption">Real sloutions to studio lightning</div>
    <div class="abs dots"><span class="dot on"></span><span class="dot"></span><span class="dot"></span><span class="dot"></span><span class="dot"></span></div>
  </div>
</section>

<section class="abs cards">
  <div class="abs card" style="left:142px">
    <h3 class="card-title" style="left:-4px">Broadcasting</h3>
    <div class="card-frame" style="left:0"><div class="card-photo" role="img" aria-label="Radio host at a studio microphone" style="background:linear-gradient(90deg,#2b3f6a,#7a8fb0,#d8b08a)"></div></div>
    <div class="card-body">Today the Northlight team has more than 150 years of investment experience among its team of more than 20 professionals across four offices.</div>
    <span class="pin" style="left:81px"></span>
    <span class="more" style="left:61px">Read More</span>
  </div>
  <div class="abs card" style="left:362px">
    <h3 class="card-title" style="left:-1px">Education</h3>
    <div class="card-frame" style="left:0"><div class="card-photo" role="img" aria-label="Classroom with rows of desks" style="background:linear-gradient(#c8ccd0,#8a9a9a 60%,#4a6a80)"></div></div>
    <div class="card-body">Northlight press releases are available to view online and/or print. Select a press release below to open the full version. Your selection will open in a new browsing window for easy reading and printing.</div>
    <span class="pin" style="left:81px"></span>
    <span class="more" style="left:61px">Read More</span>
  </div>
  <div class="abs card" style="left:589px">
    <h3 class="card-title" style="left:0">National News</h3>
    <div class="card-frame" style="left:0"><div class="card-photo" role="img" aria-label="Audience seated at a press conference" style="background:linear-gradient(#e8dcc8,#8a5a40 55%,#3a2a2a)"></div></div>
    <div class="card-body">Northlight investment interests can be categorized into three general domains: manufacturing, business services and value-added distribution.</div>
    <span class="pin" style="left:81px"></span>
    <span class="more" style="left:61px">Read More</span>
  </div>
  <div class="abs card" style="left:811px">
    <h3 class="card-title" style="left:0">Sermon Recording</h3>
    <div class="card-frame" style="left:0"><div class="card-photo" role="img" aria-label="Studio microphone against a blue sound wave" style="background:linear-gradient(90deg,#0a3a5a,#1a8ab8,#0a2a40)"></div></div>
    <div class="card-body">Northlight investment interests can be categorized into three general domains: manufacturing, business services and value-added distribution.</div>
    <span class="pin" style="left:81px"></span>
    <span class="more" style="left:61px">Read More</span>
  </div>
</section>

<div class="abs divider"></div>
<h2 class="abs news-title">Latest News</h2>
<div class="abs product-frame"><div class="product-photo" role="img" aria-label="Four-lamp fluorescent studio light fixture"></div></div>
<p class="abs posted">Posted on : 7th January 2012<br>Posted in : Dark lights</p>
<h3 class="abs product-name">Introducing the 4CB320</h3>
<ul class="abs features">
  <li>Same price as the 2CB320, but</li>
  <li>more light output</li>
  <li>more even distribution of light</li>
  <li>lighter aluminum construction</li>
  <li>semi-specular reflector</li>
  <li>inner two-lamp, outer-two lamp, all four lamp bank</li>
  <li>switchability</li>
  <li>vertical or horizontal mounting</li>
</ul>

<form class="abs newsletter">
  <h2 class="nl-head">Newsletter</h2>
  <p class="nl-sub">Join our bi-monthly email newsletter for the latest offer</p>
  <label class="field-label" style="top:174px;top:101px">Name:</label>
  <span class="field" style="top:89px"></span>
  <label class="field-label" style="top:162px">E-mail:</label>
  <span class="field" style="top:149px"></span>
  <button class="subscribe" type="button">Subscribe</button>
</form>

<footer class="abs footer">
  <nav><a href="#">Home</a><a href="#">About Us</a><a href="#">Products</a><a href="#">Latest News</a><a href="#">Contact Us</a></nav>
  <p>Copyright 2012. All Rights Reserved</p>
</footer>
</body>
</html>
```